Bright Leaf Company Needs New Packaging Design

We need a design to print directly on our stand up zip pouches, 6x9x3 in., to replace the labels we were applying on generic matte black pouches.

We'd like to keep the current color theme of matte black + [Flavor Color] (in this case, fushia) to communicate the idea of modern, luxury brand (please see velcorra coffee brand) and stay somewhat close to the current label so our product will be recognized by actual customers. Other flavors will be a declination of the same layout, matte black + [flavor color]. Colors used should be vibrant, eye catching, to stand out from competition.

We also want to display the actual tea blend picture on the packaging so the consumer can see how beautiful the tea is. The font size for Amber Orchard Meadow should be big enough so it's readable when the product is seen in thumbnail format.

The front should have a seal/stamp close to a top corner with a big "100% Freshness Guarantee",

The company logo "The Lumo Company" should be present on the front in a prominent spot. It's provided in the zip file from old label.

We need to display the net weight (4oz / 113g) and number of servings (makes 60 cups). Please refer to old label.

On the back side we need a space for the UPC barcode at the bottom, the company address, a space for the brand's story/mission, steeping instructions with icons (see current label), ingredients and another section featuring our other products. All fonts should be 10pt or bigger.

Artwork of the current label current label is available here
https://files.zentrovault.example/folders/7Qx2mRpL4vNa8sKd1TyHwBcE?resourcekey=0-Fk39LwQpz8RnVt2XyMbCaJ&usp=sharing

Target Market(s)

USA market, Women ages 25-45, young & young at heart, trendy, health conscious, luxury

Industry/Entity Type

Premium Loose Leaf Tea

Font styles to use
Other font styles liked:
• fonts provided in zip file

Colors
E54698
E96AAD
F1A4CE
F9D9EA
FCEFF6

Requirements
Must have
• See description
Should not have
• Asian look and feel

```html
<!DOCTYPE html>
<html lang="en">
<head>
<meta charset="utf-8">
<title>Amber Orchard Meadow Tea – Pouch Front</title>
<link href="https://fonts.googleapis.com/css2?family=Lora:ital,wght@1,600&family=Montserrat:wght@400;500;600&display=swap" rel="stylesheet">
<style>
  :root {
    --backdrop: #a62a74;
    --pouch-black: #0b0b0b;
    --label-black: #121212;
    --label-edge: #262626;
    --fuchsia-light: #b3307e;
    --fuchsia-deep: #6f1249;
    --white: #ffffff;
    --soft-white: #e9e9e9;
    --muted: #bdbdbd;
    --organic-green: #1f7a3e;
  }
  * { margin: 0; padding: 0; box-sizing: border-box; }
  html, body { width: 848px; height: 1200px; overflow: hidden; }
  body {
    background: var(--backdrop);
    font-family: "Montserrat", Arial, sans-serif;
    color: var(--white);
    position: relative;
  }
  .pouch {
    position: absolute; left: 36px; top: 0; width: 776px; height: 1200px;
    background: var(--pouch-black);
    border-radius: 14px 14px 4px 4px;
    overflow: hidden;
  }
  .label {
    position: absolute; left: 37px; top: 172px; width: 705px; height: 960px;
    background: var(--label-black);
    border: 1px solid var(--label-edge);
  }
  .label-field { position: absolute; left: 0; top: 0; width: 705px; height: 960px; }
  .abs { position: absolute; }
  .tagline {
    left: 0; width: 776px; top: 222px; text-align: center;
    font-family: "Lora", Georgia, serif; font-style: italic; font-weight: 600;
    font-size: 28px; letter-spacing: 0.5px; color: var(--soft-white);
  }
  .ribbon { left: 187px; top: 277px; width: 394px; height: 44px; }
  .ribbon-text {
    left: 187px; width: 394px; top: 288px; text-align: center;
    font-size: 18px; font-weight: 500; letter-spacing: 2.4px; color: var(--soft-white);
  }
  .product-name {
    left: 0; width: 776px; top: 340px; text-align: center;
    font-weight: 600; font-size: 44px; line-height: 52px; letter-spacing: 1px;
  }
  .fresh-seal { left: 604px; top: 217px; width: 104px; height: 104px; }
  .fresh-seal-text {
    left: 604px; top: 238px; width: 104px; text-align: center;
    font-size: 14px; font-weight: 500; line-height: 16px;
  }
  .fresh-seal-text .big { font-size: 17px; }
  .brand {
    left: 100px; top: 520px; width: 290px;
    display: flex; align-items: center; gap: 12px;
  }
  .brand-dot { width: 18px; height: 18px; border-radius: 50%; background: var(--white); flex: none; }
  .brand-name { font-size: 30px; font-weight: 600; line-height: 36px; color: var(--white); }
  .blend-photo {
    left: 64px; top: 600px; width: 405px; height: 382px;
    border-radius: 48% 52% 40% 46% / 18% 30% 55% 60%;
    background:
      radial-gradient(circle at 30% 40%, #e6c23a 0 18%, transparent 40%),
      radial-gradient(circle at 65% 60%, #b8322b 0 12%, transparent 35%),
      radial-gradient(circle at 45% 75%, #7d6aa0 0 10%, transparent 30%),
      linear-gradient(135deg, #d9a834, #a4442c 55%, #5a3d5e);
  }
  .icon { stroke: var(--soft-white); fill: none; stroke-width: 1.6; }
  .info { text-align: center; font-size: 8.5px; line-height: 10.5px; color: var(--muted); }
  .info b { color: var(--soft-white); font-weight: 600; }
  .net-weight { left: 450px; top: 883px; width: 132px; text-align: center; font-size: 14px; line-height: 18px; color: var(--soft-white); }
  .badge-circle {
    border: 1.6px solid var(--soft-white); border-radius: 50%;
    display: flex; flex-direction: column; align-items: center; justify-content: center;
    text-align: center;
  }
  .organic-badge {
    left: 474px; top: 950px; width: 72px; height: 72px; border-radius: 50%;
    background: var(--white); border: 5px solid var(--organic-green);
  }
  .caffeine { left: 579px; top: 945px; width: 76px; height: 76px; font-size: 13px; line-height: 15px; }
  .cups { left: 574px; top: 1036px; width: 72px; height: 72px; }
  .cups .num { font-size: 22px; font-weight: 600; line-height: 22px; }
  .cups .unit { font-size: 11px; }
  .ingredients {
    left: 128px; top: 994px; width: 300px;
    font-size: 12px; line-height: 17px; color: var(--soft-white);
  }
  .ingredients b { font-weight: 600; color: var(--white); }
</style>
</head>
<body>
  <div class="pouch">
    <div class="label">
      <svg class="label-field" viewBox="0 0 705 960" aria-hidden="true">
        <defs>
          <linearGradient id="fuchsiaWash" x1="0" y1="0" x2="1" y2="1">
            <stop offset="0" stop-color="#a5286f"/>
            <stop offset="0.45" stop-color="#8c1d5e"/>
            <stop offset="1" stop-color="#5e0f3e"/>
          </linearGradient>
        </defs>
        <path d="M0 0 H705 V470 C650 600 500 610 430 520 C380 455 300 425 0 440 Z" fill="url(#fuchsiaWash)"/>
        <path d="M705 470 C650 600 500 610 430 520" fill="none" stroke="#0b0b0b" stroke-width="14"/>
      </svg>
    </div>

    <p class="abs tagline">Calming &amp; soothing</p>

    <svg class="abs ribbon" viewBox="0 0 394 44" aria-hidden="true">
      <path d="M4 2 H390 L378 22 L390 42 H4 L16 22 Z" fill="none" stroke="#e9e9e9" stroke-width="2"/>
    </svg>
    <p class="abs ribbon-text">PREMIUM LOOSE HERBAL TEA</p>

    <h1 class="abs product-name">Amber Orchard<br>Meadow Tea</h1>

    <svg class="abs fresh-seal" viewBox="0 0 104 104" aria-hidden="true">
      <circle cx="52" cy="52" r="48" fill="none" stroke="#e9e9e9" stroke-width="2" stroke-dasharray="60 12"/>
      <circle cx="52" cy="52" r="51" fill="none" stroke="#e9e9e9" stroke-width="1" stroke-dasharray="40 30"/>
    </svg>
    <p class="abs fresh-seal-text"><span class="big">100%</span><br>Freshness<br>Guarantee<br><span class="big">Free</span></p>

    <div class="abs brand">
      <span class="brand-dot"></span>
      <span class="brand-name">The Lumo Company</span>
    </div>

    <div class="abs blend-photo" role="img" aria-label="Photo of the loose tea blend: dried chamomile buds, rose petals, lavender and rosehips"></div>

    <svg class="abs" style="left:506px;top:778px" width="22" height="42" viewBox="0 0 22 42" aria-hidden="true">
      <rect class="icon" x="6" y="2" width="7" height="28" rx="3.5"/>
      <circle class="icon" cx="9.5" cy="35" r="5.5"/>
      <path class="icon" d="M15 8 h4 M15 12 h3 M15 16 h4 M15 20 h3"/>
    </svg>
    <p class="abs info" style="left:456px;top:826px;width:120px"><b>Temperature:</b><br>206° F / 95° C</p>

    <svg class="abs" style="left:604px;top:778px" width="44" height="22" viewBox="0 0 44 22" aria-hidden="true">
      <path class="icon" d="M2 3 L26 13"/>
      <ellipse class="icon" cx="33" cy="15" rx="9" ry="5.5" transform="rotate(18 33 15)"/>
    </svg>
    <p class="abs info" style="left:563px;top:810px;width:126px"><b>Quantity Per Cup:</b><br>1-2 Heaping<br>Teaspoon</p>

    <p class="abs net-weight">Net Weight<br>4 oz. 113 g</p>

    <svg class="abs" style="left:613px;top:862px" width="24" height="28" viewBox="0 0 24 28" aria-hidden="true">
      <circle class="icon" cx="12" cy="16" r="10"/>
      <circle class="icon" cx="12" cy="16" r="6.5"/>
      <path class="icon" d="M12 16 V12 M12 16 h3 M9 2 h6 M12 2 v4 M20 6 l2 -2"/>
    </svg>
    <p class="abs info" style="left:563px;top:902px;width:126px"><b>Steeping Time:</b><br>5-7 Mins</p>

    <div class="abs organic-badge" role="img" aria-label="Organic certification seal"></div>

    <div class="abs badge-circle caffeine">Caffeine<br>Free</div>
    <div class="abs badge-circle cups"><span class="num">60</span><span class="unit">cups</span></div>

    <p class="abs ingredients"><b>Ingredient:</b> Organic chamomile, organic lavender, organic roses, organic rosehips.</p>
  </div>
</body>
</html>
```